Property Services Company Needs a Brochure Design

Looking for a new brochure design for an existing property services company.

We provide a range of property services from, market research, real estate brokerage, valuation and appraisal, property development and other real estate consulting services.

We would like a fresh modern brochure design with good graphics and features. Our colours are white, blue and orange.

The design should communicate, attention to detail, superior service delivery and distinction in results.
Updates

I would like the brochure to be roughly about 20 pages.

Containing the following,

1) An introduction
2) Contents Page
2) What we do
3) Our Services
4) Agency & Brokerage
5) Real Estate Consulting
6) Market Research
7) Appraisal & Valuation
8) Project Management
9) Property Development

I would also like icons to represent items 4,5,6,7,8 & 9, they should be represented vertically on each of the pages from the contents page and highlighted individually on the pages that they represent.. i.e. on appraisal & valuation page, all six icons will be arranged vertically and the appraisal and valuations icon will be highlighted.

I will also like to have images that depict the services on the various pages.

I have some pages I think will flow which I will upload shortly.

Industry/Entity Type

Real Estate

Font styles to use
Serif

Colors
f78f20
0455a3

```html
<!DOCTYPE html>
<html lang="en">
<head>
<meta charset="utf-8">
<title>Services Spread – Property Brochure</title>
<link rel="stylesheet" href="https://fonts.googleapis.com/css2?family=Tinos:ital,wght@0,400;0,700;1,400&display=swap">
<style>
  :root{
    --navy:#3a2d6c;
    --orange:#e56f1f;
    --ink:#3c3c3c;
    --paper:#ffffff;
    --paper-shade:#ececee;
    --backdrop:#d9d9d9;
    --photo-sky:#8fb4d6;
    --photo-suit:#5a5f6a;
    --photo-wall:#c9ccd1;
    --building-light:#f3f3f3;
    --building-dark:#c7c7c9;
  }
  *{box-sizing:border-box;margin:0;padding:0}
  html,body{width:1200px;height:800px;overflow:hidden}
  body{background:var(--backdrop);font-family:"Tinos","Times New Roman",serif;color:var(--ink)}
  .spread{position:absolute;left:80px;top:20px;width:1040px;height:760px;display:flex}
  .page{position:relative;width:520px;height:760px;overflow:hidden;
    background:linear-gradient(180deg,var(--paper) 0%,var(--paper) 55%,var(--paper-shade) 100%)}
  .page--left{border-right:1px solid #d4d4d6}
  .photo{position:absolute;z-index:0}
  .building-mark{position:absolute}

  /* left page */
  .photo--architect{left:0;top:0;width:334px;height:270px;
    background:linear-gradient(135deg,var(--photo-wall) 0%,#a9adb5 45%,var(--photo-suit) 100%)}
  .page--left .building-mark{left:372px;top:50px;width:80px;height:140px}
  .section-title{position:absolute;left:340px;top:196px;font-size:30px;font-weight:700;
    color:var(--navy);letter-spacing:.5px}
  .rule-orange{position:absolute;height:4px;background:var(--orange)}
  .page--left .rule-orange{left:334px;right:0;top:232px}
  .service-card{position:absolute;z-index:2;color:#fff;padding:11px 10px;font-size:11px;line-height:13.6px}
  .service-card h3{font-weight:400;font-size:14px;margin-bottom:6px}
  .service-card--navy{background:var(--navy)}
  .service-card--orange{background:var(--orange)}
  .card-agency{left:38px;top:270px;width:155px;height:350px}
  .card-consulting{left:203px;top:274px;width:152px;height:296px}
  .card-research{left:365px;top:278px;width:151px;height:336px}
  .photo--reader{left:64px;top:540px;width:383px;height:220px;
    background:radial-gradient(ellipse at 50% 45%,#e6e2da 0%,#b9b3a8 45%,#3f4b63 100%)}
  .rule-navy{position:absolute;z-index:3;left:0;right:0;height:4px;background:var(--navy)}
  .page--left .rule-navy{top:722px}

  /* right page */
  .page--right .building-mark{left:50px;top:38px;width:92px;height:190px}
  .photo--team{left:199px;top:0;width:321px;height:222px;
    background:linear-gradient(160deg,var(--photo-sky) 0%,#b8cbe0 40%,#c9c56a 70%,#7d8794 100%)}
  .page--right .rule-orange{left:0;right:0;top:230px}
  .text-col{position:absolute;font-size:10.8px;line-height:13.2px;color:var(--ink)}
  .text-col p{margin-bottom:4px}
  .col-services{left:30px;top:248px;width:160px}
  .col-about{left:203px;top:248px;width:290px}
  .subhead{font-weight:700;font-size:13.5px;line-height:14.5px;margin:3px 0 4px}
  .subhead--navy{color:var(--navy)}
  .subhead--orange{color:var(--orange)}
  .page--right .rule-navy{top:704px}
</style>
</head>
<body>
<main class="spread">
  <section class="page page--left">
    <div class="photo photo--architect" role="img" aria-label="Photo of a businessman in a hard hat reading building plans"></div>
    <div class="building-mark" role="img" aria-label="Outline graphic of tall office towers" style="background:linear-gradient(90deg,var(--building-light),var(--building-dark))"></div>
    <h2 class="section-title">SERVICES</h2>
    <div class="rule-orange"></div>

    <div class="photo photo--reader" role="img" aria-label="Photo of a smiling businessman reading a newspaper on a sofa"></div>

    <article class="service-card service-card--navy card-agency">
      <h3>Agency&amp; Brokerage</h3>
      <p>The brokerage team, covers both landlords and tenants across the residential and commercial markets. With a large database of industry specific individuals and corporate twinned with a large database of inventory, we are able to very quickly understand the needs of our clients and find the perfect fit. We enjoy long standing relationships with many of our clients and landlords, and are always happy to meet with new clients to advise on how best to maximize their rental return or budget.</p>
    </article>

    <article class="service-card service-card--orange card-consulting">
      <h3>Consulting</h3>
      <p>We provide a broad range of consulting services, we understand that out client needs may vary and our experienced team are at hand to provide tailored solutions to their needs. Our professional services include corporate planning, feasibility studies, market studies, due diligence, property tax, litigation, asset review and framework for foreign direct investment.</p>
    </article>

    <article class="service-card service-card--navy card-research">
      <h3>Market Research</h3>
      <p>Our market research team, regularly conduct surveys across a wide range of areas in both the commercial and residential markets. They regularly produce market reports that can be used for a wide range of purposes. This information also provides our team members with superior knowledge of market trends, price shifts, occupancy rates and other unique trends. The information provided allows us to provide information useful for forecasting growth and trends in the market.</p>
    </article>

    <div class="rule-navy"></div>
  </section>

  <section class="page page--right">
    <div class="building-mark" role="img" aria-label="Outline graphic of tall office towers" style="background:linear-gradient(90deg,var(--building-light),var(--building-dark))"></div>
    <div class="photo photo--team" role="img" aria-label="Photo of three engineers in hard hats and safety vests reviewing plans on site"></div>
    <div class="rule-orange"></div>

    <div class="text-col col-services">
      <h3 class="subhead subhead--navy">Project Management&amp; Property Development</h3>
      <p>Our project management team, with vast experience across commercial and residential developments provide the much needed support to achieve your dream property or office, allowing our clients to concentrate on their core business. We provide accurate information from financing, to design concept to budgeting and construction management. We take pride in creating inspirational developments that people can live, work and enjoy, whilst adding value.</p>
      <h3 class="subhead subhead--orange">Valuation &amp; Appraisal</h3>
      <p>We provide valuation and appraisal services to clients across a broad spectrum. Our valuation advice can provide information to assist with portfolio valuation, single asset valuation, financial reporting valuation. These services are provided to individuals, financial institutions and corporates. Appraisal methods will vary based on the specific needs of our clients</p>
    </div>

    <div class="text-col col-about">
      <h3 class="subhead subhead--orange">WHAT WE DO</h3>
      <p>Halvorsen is a leading property services company, incorporated in 1984, providing bespoke solutions in advisory, brokerage and turnkey solutions to owners, occupiers and property investors. Over the years we have expanded our services with a foundation based on core strengths, unrivalled local expertise, network and knowledge combined with strategic partnership. As well as providing property solutions we also develop commercial and residential units.</p>
      <p>Our growth has been based on maintaining relationships with our extensive client base, ranging from financial institutions, government agencies, airlines and servicing companies, manufacturing companies, multinationals and local</p>
      <p>corporations, to private developers and investors. Our clients depend on our ability to draw on years of experience in the local market, our professionals know their communities and the property market inside and out, and provide knowledgeable, creative solutions to all their real estate needs.</p>
      <p>The combination of our integrated services allows us to provide a superior end to end solution to our clients, customized to their own requirements. Market research is a core component to our business model, allowing us to make informed decisions based based on research findings. Our brokerage team also benefits from this information, allowing our associates to advise clients on how best to maximise return on their investment on the sale or buy side within a short timeline.</p>
      <p>We pay great attention to detail in consideration of our client requirements, delivering mandates with distinction.</p>
    </div>

    <div class="rule-navy"></div>
  </section>
</main>
</body>
</html>
```